Creation of a cover for a novel on immigration in Paris, with one of the two joined images. These photos can be modified (shape, colors…)
Size: 14 x 20.5 cm (vertical) with 5 mm bleed on the top, bottom and right areas.

TITLE: "Teodor, the Wanderer" (and not "African immigrant in Paris)
AUTHOR: “Lucien Marvaud”
NOTICES TO BE ADDED:
- “Novel” (witch means novel)
- “Preface by Solenne Varek” (the preface writer)
PUBLISH “Editions Pluvane” (AT THE BOTTOM OF THE PAGE)

Target Market(s)

Book shops

Industry/Entity Type

Book cover

Requirements
Must have
• One of the two images joined

```html
<!DOCTYPE html>
<html lang="en">
<head>
<meta charset="utf-8">
<title>Teodor, the Wanderer — Book Cover</title>
<link rel="stylesheet" href="https://fonts.googleapis.com/css2?family=Roboto+Condensed:wght@400;700&family=Montserrat:wght@600&family=Roboto:wght@500&display=swap">
<style>
  :root {
    --backdrop: #ececec;
    --cover-black: #141414;
    --title-yellow: #f4f41c;
    --text-white: #ffffff;
    --scene-amber: #b8672a;
    --scene-dusk: #2a4a5c;
    --scene-deep: #1a2a33;
  }
  * { margin: 0; padding: 0; box-sizing: border-box; }
  html, body {
    width: 1200px;
    height: 1200px;
    overflow: hidden;
    background: var(--backdrop);
  }
  .cover {
    position: absolute;
    left: 320px;
    top: 168px;
    width: 560px;
    height: 864px;
    background: var(--cover-black);
    color: var(--text-white);
    overflow: hidden;
  }
  .preface {
    position: absolute;
    top: 44px;
    width: 100%;
    text-align: center;
    font-family: "Roboto", sans-serif;
    font-weight: 500;
    font-size: 22px;
    letter-spacing: 0.5px;
  }
  .station-scene {
    position: absolute;
    left: 42px;
    top: 362px;
    width: 462px;
    height: 392px;
    background:
      linear-gradient(180deg, rgba(20,20,20,0) 55%, rgba(20,20,20,0.55) 100%),
      linear-gradient(90deg, var(--scene-amber) 0%, #7a4a2a 38%, var(--scene-deep) 55%, var(--scene-dusk) 100%);
    -webkit-mask-image: radial-gradient(ellipse 60% 55% at 50% 50%, #000 55%, transparent 100%);
    mask-image: radial-gradient(ellipse 60% 55% at 50% 50%, #000 55%, transparent 100%);
  }
  .title {
    position: absolute;
    top: 92px;
    width: 100%;
    text-align: center;
    font-family: "Roboto Condensed", sans-serif;
    color: var(--title-yellow);
    line-height: 1;
  }
  .title-first {
    display: block;
    font-weight: 400;
    font-size: 140px;
    letter-spacing: -1px;
  }
  .title-joiner {
    display: flex;
    align-items: center;
    justify-content: center;
    gap: 22px;
    margin-top: 8px;
    font-weight: 400;
    font-size: 40px;
    color: var(--text-white);
  }
  .title-joiner .rule {
    width: 170px;
    height: 2px;
    background: var(--text-white);
  }
  .title-second {
    display: block;
    margin-top: 8px;
    font-weight: 700;
    font-size: 98px;
    letter-spacing: -0.5px;
  }
  .author {
    position: absolute;
    top: 733px;
    width: 100%;
    text-align: center;
    font-family: "Montserrat", sans-serif;
    font-weight: 600;
    font-size: 36px;
    letter-spacing: 2.5px;
  }
  .publisher {
    position: absolute;
    top: 786px;
    width: 100%;
    text-align: center;
    font-family: "Roboto", sans-serif;
    font-weight: 500;
    font-size: 32px;
    letter-spacing: 0.5px;
  }
</style>
</head>
<body>
  <main class="cover">
    <p class="preface">PREFACE BY SOLENNE VAREK</p>
    <div class="station-scene" role="img" aria-label="Photograph of a lone traveller with a backpack and bag seen from behind on a misty night train platform, warm amber lights on the left and cold blue light on the right"></div>
    <h1 class="title">
      <span class="title-first">TEODOR</span>
      <span class="title-joiner"><span class="rule"></span>THE<span class="rule"></span></span>
      <span class="title-second">WANDERER</span>
    </h1>
    <p class="author">LUCIEN MARVAUD</p>
    <p class="publisher">EDITIONS PLUVANE</p>
  </main>
</body>
</html>
```